Print & digital package needed for technology firm

We need a package of coordinating marketing materials for our technology business. We offer technology solutions to midsized organizations, including data center, outsourced IT, and technology consulting. Find more information on our website, www.pexlora.com. Design is the main concern, we can modify the text ongoing to best reflect our company’s offerings. The design should communicate technology expertise and strategic thinking. Our website is currently being updated with a “flat design” theme and we’d like design of these items to be flat, fresh, modern, and professional, without being boring.
Please use attached logo - can send in .ai/.eps/.psd/etc. Fonts in logo are Futura, Futura Book, and Lato. Please use pexlora blue, #0372bb.
Please find attached one of our product flyers for one of the computers we lease. Fonts used are Roboto Slab (partial to this font) & Lato. Also attached copy of our business card design.
Taglines we have used include “Does IT hear what troubles you?” and “IT made simple” although we are open to new ideas.
Would like final products to be available in editable files - .psd/.tif/.ai/etc.

- 1 PowerPoint template
- 1 leaderboard ad (digital, 72dpi)
- 1 medium rectangle ad 300x250 (digital, 72dpi)
- 1 full page ad 8x11 (print, 300dpi)
- 1 half-page ad horizontal (print, 300dpi)
- 1 letterhead template
- 1 proposal front-page

There is potential for further graphic/print design opportunities for our business as well.

All, thank you for your assistance in understanding the budget process with this type of design contest - we have updated the project's budget to reflect the items we are requesting.

Please email mvarga at pexlora.com with inquiries or comments. Thank you.

Designers,

Due to an oversight, our project was listed as "refundable" - this has been corrected and changed to committed payment.
To enter into this contest, please pick 2-3 items from the list of desired materials (ads, powerpoint, letterhead, etc.) It is not necessary to submit all items which will be part of the final package to be considered for the contest.

Thank you. Please contact mvarga@pexlora.com for questions.
Best,
Mimi

CEOs, CFOs, CIOs, COOs - college+ educated, 30-60, professional.

```html
<!DOCTYPE html>
<html lang="en">
<head>
<meta charset="utf-8">
<title>Pexlora Letterhead</title>
<link rel="stylesheet" href="https://fonts.googleapis.com/css2?family=Jost:wght@300;400;500&family=Lato:wght@400&display=swap">
<style>
  :root {
    --brand-blue: #0372bb;
    --brand-blue-dark: #03508a;
    --paper: #ffffff;
    --rule-grey: #b9b9b9;
    --tagline-grey: #7d7d7d;
    --footer-black: #000000;
    --canvas: #ffffff;
  }
  * { box-sizing: border-box; margin: 0; padding: 0; }
  html, body {
    width: 1200px; height: 1000px; overflow: hidden;
    background: var(--canvas);
  }
  .letterhead {
    position: absolute; left: 272px; top: 33px;
    width: 655px; height: 928px;
    background: var(--paper);
    box-shadow: 0 2px 8px rgba(0,0,0,0.35);
    overflow: hidden;
  }
  .header-band {
    position: absolute; left: 0; top: 0; width: 100%; height: 140px;
    background: var(--brand-blue);
    border-bottom: 4px solid var(--brand-blue-dark);
  }
  .header-rule {
    position: absolute; left: 0; top: 144px; width: 100%; height: 4px;
    background: var(--rule-grey);
  }
  .name-plate {
    position: absolute; left: 379px; top: 23px; width: 257px; height: 98px;
    background: var(--paper); border-radius: 10px;
    box-shadow: 0 4px 0 var(--brand-blue-dark);
    text-align: center;
  }
  .company-name {
    font-family: 'Jost', sans-serif; font-weight: 500;
    font-size: 42px; line-height: 1; color: var(--brand-blue);
    margin-top: 15px;
  }
  .service-line {
    font-family: 'Lato', sans-serif; font-size: 10.5px;
    color: var(--tagline-grey); margin-top: 12px;
  }
  .footer-band {
    position: absolute; left: 0; bottom: 0; width: 100%; height: 67px;
    background: var(--footer-black); color: var(--paper);
    font-family: 'Jost', sans-serif;
  }
  .contact-line {
    position: absolute; left: 10px; display: flex; align-items: center;
    font-weight: 300; font-size: 21px; line-height: 1; letter-spacing: 0.3px;
  }
  .contact-line svg { margin-right: 4px; }
  .contact-phone { top: 9px; }
  .contact-web { top: 41px; }
  .footer-divider {
    position: absolute; left: 524px; top: 7px; width: 1px; height: 53px;
    background: var(--paper);
  }
  .postal-address {
    position: absolute; right: 14px; top: 9px;
    font-style: normal; text-align: right;
    font-size: 11.5px; line-height: 12.5px; font-weight: 400;
  }
</style>
</head>
<body>
  <main class="letterhead">
    <header>
      <div class="header-band"></div>
      <div class="header-rule"></div>
      <div class="name-plate">
        <div class="company-name">pexlora</div>
        <div class="service-line">IT Consulting &nbsp;|&nbsp; Managed Services &nbsp;|&nbsp; Data Center</div>
      </div>
    </header>
    <footer class="footer-band">
      <div class="contact-line contact-phone">
        <svg width="14" height="18" viewBox="0 0 14 18" aria-hidden="true">
          <path d="M4 1 L7 1 L8 5 L6 6.5 C6.5 9 7.5 11 9 12.5 L11 11.5 L13 14.5 L11 16.8 C6 16 2.5 10 2.5 3.5 Z" fill="#fff"/>
        </svg>
        <span>301 555 0147</span>
      </div>
      <div class="contact-line contact-web">
        <svg width="19" height="19" viewBox="0 0 20 20" aria-hidden="true">
          <circle cx="10" cy="10" r="9" fill="#fff"/>
          <path d="M5 5 C7 4 9 5 8 7 C7 9 4 8 5 11 C6 13 8 12 8 15 L7 18 C3.5 16.5 2 13 2.5 9 Z M12 3 C14 4 15 6 13.5 7 C12 8 13 10 15 10 C17 10 17 12 16 14 C15 16 13 17 12 16 C11.5 14 13 13 11.5 11.5 C10 10 10.5 7 12 6 Z" fill="#000"/>
        </svg>
        <span>pexlora.com</span>
      </div>
      <div class="footer-divider"></div>
      <address class="postal-address">
        48 Harbor Lane<br>
        Suite 210<br>
        Rockvale<br>
        MD 20811
      </address>
    </footer>
  </main>
</body>
</html>
```